I'm looking for an edgy and contemporary book cover rebranding

I have nearly completed a revised edition of my book 'GRIEF AWAY NOW" that was published in 2019. The book helped readers struggling with the shame associated with their mental health challenges.

Several of my readers encouraged me to adapt the book to younger readers - teenagers. I am now in the process of rewriting my book for teenage readers: 'GRIEF AWAY NOW - FOR TEENAGERS.'

Ideally the book cover should look similar, yet with a 'youth edge' to the design.

Grief Away Now 4 teens or for teens

Grief Away Now 4 teenagers or for teenagers.

Please keep the photo but make in more abstract - see attached example (Rise-higher with Tobin Vael).

Target Market(s)

Teenagers and possibly parents of teenagers

Industry/Entity Type

Mental health and wellbeing

Font styles to use
Sans Serif

Colors

Designer to choose colors to be used in the design.

Requirements
Must have
• There is a connection to the first edition of my book and appeals to young readers
Nice to have
• Contemporary and youthful design that connects with the first edition.
Should not have
• Cover looks childish or feminine

```html
<!DOCTYPE html>
<html lang="en">
<head>
<meta charset="utf-8">
<title>Grief Away Now – For Teenagers | Book Cover</title>
<link rel="stylesheet" href="https://fonts.googleapis.com/css2?family=League+Spartan:wght@400;700;800&family=Montserrat:wght@400;700&display=swap">
<style>
  :root {
    --page-bg: #e8e8e8;
    --cover-light: #c9c9c7;
    --cover-mid: #9d9d9b;
    --cover-dark: #6f6f6d;
    --ink: #121212;
    --ink-warm: #3b2e28;
    --author-ink: #161616;
  }
  * { margin: 0; padding: 0; box-sizing: border-box; }
  html, body {
    width: 1200px;
    height: 848px;
    overflow: hidden;
    background: var(--page-bg);
  }
  .canvas {
    position: relative;
    width: 1200px;
    height: 848px;
  }
  .book-cover {
    position: absolute;
    left: 380px;
    top: 112px;
    width: 440px;
    height: 624px;
    overflow: hidden;
  }
  .cover-artwork {
    position: absolute;
    inset: 0;
    background:
      radial-gradient(ellipse at 30% 20%, var(--cover-light) 0%, transparent 60%),
      linear-gradient(160deg, var(--cover-light) 0%, var(--cover-mid) 45%, var(--cover-dark) 100%);
  }
  .author-name {
    position: absolute;
    top: 42px;
    left: 0;
    width: 100%;
    text-align: center;
    font-family: "Montserrat", sans-serif;
    font-size: 27px;
    letter-spacing: 0.2em;
    color: var(--author-ink);
  }
  .author-name .first { font-weight: 700; }
  .author-name .last { font-weight: 400; }
  .cover-title {
    position: absolute;
    left: 0;
    top: 0;
    width: 440px;
    height: 624px;
  }
  .cover-title text {
    font-family: "League Spartan", sans-serif;
    font-weight: 800;
  }
  .publisher-mark {
    position: absolute;
    left: 0;
    bottom: 18px;
    width: 100%;
    display: flex;
    align-items: center;
    justify-content: center;
    gap: 6px;
    font-family: "League Spartan", sans-serif;
    font-weight: 700;
    font-size: 13px;
    color: var(--ink);
  }
  .publisher-mark .dot {
    width: 10px;
    height: 10px;
    border-radius: 50%;
    background: var(--ink);
  }
</style>
</head>
<body>
<main class="canvas">
  <section class="book-cover">
    <div class="cover-artwork" role="img" aria-label="Abstract grey brushed texture with streaks of light"></div>

    <p class="author-name"><span class="first">DALE</span> <span class="last">HARTWELL</span></p>

    <svg class="cover-title" viewBox="0 0 440 624" aria-label="Grief Away Now – For Teenagers">
      <defs>
        <linearGradient id="title-ink" x1="0" y1="0" x2="1" y2="0">
          <stop offset="0" stop-color="var(--ink)"/>
          <stop offset="0.55" stop-color="var(--ink)"/>
          <stop offset="0.8" stop-color="var(--ink-warm)"/>
          <stop offset="1" stop-color="var(--ink)"/>
        </linearGradient>
      </defs>
      <text x="30" y="300" font-size="118" textLength="380" lengthAdjust="spacingAndGlyphs" fill="url(#title-ink)">GRIEF</text>
      <text x="30" y="378" font-size="90" textLength="380" lengthAdjust="spacingAndGlyphs" fill="url(#title-ink)">AWAY NOW</text>
      <text x="32" y="436" font-size="56" textLength="376" lengthAdjust="spacingAndGlyphs" fill="url(#title-ink)">FOR TEENAGERS</text>
    </svg>

    <div class="publisher-mark">
      <span class="dot"></span>
      <span class="publisher-name">dale hartwell</span>
    </div>
  </section>
</main>
</body>
</html>
```